Accounting Practice Business Card Design

I have a logo I am happy for you to use in the design of the Business Card.
You can edit and change colours as you please, I am not fixated on it.
I am looking for a modern and clean overall feel for the finished design.

The business is a small accounting practice who thrives on word of mouth referrals and this card will be given to all current and prospect clients.

Industry/Entity Type

Accountant

Contact Information for Business Card

Marcus Elwin
Level 5, 8 Corvale Ridge Road
ASHGROVE RISE VIC 3187
Phone: 9481 3057
Email: melwin@mrfaccountants.com.au
Web: www.mrfaccountants.com.au

Font styles to use
Serif
Sans Serif

Colors
0555a3
3277b5
85acd3
0393ce
33a6d7
85cae6
00a990
33b8a4
9bcb3c

Requirements
Must have
• "The end to your tax problems begin with us"
• "A referral from you is our greatest compliment"
Nice to have
• Modern clean professional

```html
<!DOCTYPE html>
<html lang="en">
<head>
<meta charset="utf-8">
<title>MRF Accountants – Business Card</title>
<link rel="stylesheet" href="https://fonts.googleapis.com/css2?family=Open+Sans:wght@400;600;700&display=swap">
<style>
  :root {
    --page: #eaeceb;
    --paper: #ffffff;
    --blue: #2c58a6;
    --blue-deep: #284577;
    --navy: #24447a;
    --green: #386e35;
    --teal: #2f5a6a;
    --ink-light: #ffffff;
  }
  * { margin: 0; padding: 0; box-sizing: border-box; }
  html, body {
    width: 1166px; height: 1200px; overflow: hidden;
    background: var(--page);
    font-family: "Open Sans", sans-serif;
  }
  .card {
    position: absolute; left: 194px;
    width: 778px; height: 444px;
    background: var(--paper);
    overflow: hidden;
  }
  .card--front { top: 132px; }
  .card--back { top: 609px; }
  .card-shapes { position: absolute; inset: 0; width: 778px; height: 444px; }
  .holder-name {
    position: absolute; left: 95px; top: 52px;
    font-size: 35px; font-weight: 400; color: var(--ink-light); letter-spacing: .3px;
  }
  .holder-role {
    position: absolute; left: 96px; top: 90px;
    font-size: 19px; color: var(--ink-light);
  }
  .contact-list { position: absolute; left: 18px; top: 192px; list-style: none; }
  .contact-item { display: flex; align-items: center; height: 36px; margin-bottom: 8px; }
  .contact-icon { width: 46px; height: 36px; flex: none; }
  .contact-text { margin-left: 22px; font-size: 22px; color: var(--ink-light); letter-spacing: .4px; }
  .band-text {
    position: absolute; top: 374px; height: 48px; line-height: 48px;
    font-size: 20px; color: var(--ink-light);
  }
  .wordmark {
    position: absolute; text-align: center; color: var(--navy); font-weight: 700; line-height: 1;
  }
  .wordmark__name { display: block; }
  .wordmark__sub { display: block; }
  .card--front .wordmark { left: 502px; top: 186px; width: 210px; }
  .card--front .wordmark__name { font-size: 66px; letter-spacing: 2px; }
  .card--front .wordmark__sub { font-size: 21px; margin-top: 4px; letter-spacing: 1px; }
  .card--back .wordmark { left: 228px; top: 118px; width: 330px; }
  .card--back .wordmark__name { font-size: 110px; letter-spacing: 4px; }
  .card--back .wordmark__sub { font-size: 34px; margin-top: 6px; letter-spacing: 1.5px; }
</style>
</head>
<body>

<section class="card card--front">
  <svg class="card-shapes" viewBox="0 0 778 444" aria-hidden="true">
    <defs>
      <linearGradient id="front-blue" x1="0" y1="0" x2="0" y2="1">
        <stop offset="0" stop-color="#2c5aa6"/>
        <stop offset="1" stop-color="#284577"/>
      </linearGradient>
    </defs>
    <polygon points="0,0 382,0 497,444 0,444" fill="url(#front-blue)"/>
    <polygon points="382,0 484,0 420,148" fill="var(--green)"/>
    <polygon points="0,374 174,374 166,422 0,422" fill="var(--blue)"/>
    <polygon points="183,374 212,374 204,422 175,422" fill="var(--teal)"/>
    <polygon points="222,374 778,374 778,422 214,422" fill="var(--green)"/>
    <line x1="18" y1="148" x2="388" y2="148" stroke="#ffffff" stroke-width="1.5"/>
  </svg>

  <div class="holder-name">Marcus Elwin</div>
  <div class="holder-role">Accountant</div>

  <ul class="contact-list">
    <li class="contact-item">
      <svg class="contact-icon" viewBox="0 0 46 36" aria-hidden="true">
        <polygon points="0,0 36,0 46,18 36,36 0,36" fill="#fff"/>
        <path d="M11 9c2-2 4-1 5 1l1 3c0 1-1 2-2 2 1 3 3 5 5 6 0-1 1-2 2-2l3 1c2 1 2 3 0 5-3 3-9-1-12-5s-5-8-2-11z" fill="var(--navy)"/>
      </svg>
      <span class="contact-text">9481 3057</span>
    </li>
    <li class="contact-item">
      <svg class="contact-icon" viewBox="0 0 46 36" aria-hidden="true">
        <polygon points="0,0 36,0 46,18 36,36 0,36" fill="#fff"/>
        <rect x="9" y="11" width="21" height="14" rx="1.5" fill="none" stroke="var(--navy)" stroke-width="1.6"/>
        <polyline points="9.5,12 19.5,19.5 29.5,12" fill="none" stroke="var(--navy)" stroke-width="1.6"/>
      </svg>
      <span class="contact-text">melwin@mrfaccountants.com.au</span>
    </li>
    <li class="contact-item">
      <svg class="contact-icon" viewBox="0 0 46 36" aria-hidden="true">
        <polygon points="0,0 36,0 46,18 36,36 0,36" fill="#fff"/>
        <g fill="none" stroke="var(--navy)" stroke-width="1.4">
          <circle cx="19.5" cy="18" r="9"/>
          <ellipse cx="19.5" cy="18" rx="4" ry="9"/>
          <line x1="10.5" y1="18" x2="28.5" y2="18"/>
          <line x1="12" y1="13" x2="27" y2="13"/>
          <line x1="12" y1="23" x2="27" y2="23"/>
        </g>
      </svg>
      <span class="contact-text">www.mrfaccountants.com.au</span>
    </li>
  </ul>

  <div class="wordmark">
    <span class="wordmark__name">MRF</span>
    <span class="wordmark__sub">ACCOUNTANTS</span>
  </div>

  <div class="band-text" style="left:247px;">Level 5, 8 Corvale Ridge Road Ashgrove Rise Vic 3187</div>
</section>

<section class="card card--back">
  <svg class="card-shapes" viewBox="0 0 778 444" aria-hidden="true">
    <defs>
      <linearGradient id="back-blue" x1="0" y1="0" x2="0" y2="1">
        <stop offset="0" stop-color="#2c5aa6"/>
        <stop offset="1" stop-color="#284577"/>
      </linearGradient>
    </defs>
    <polygon points="0,0 32,0 148,444 0,444" fill="url(#back-blue)"/>
    <polygon points="32,0 134,0 70,147" fill="var(--green)"/>
    <polygon points="0,374 175,374 165,422 0,422" fill="var(--blue)"/>
    <polygon points="186,374 778,374 778,422 178,422" fill="var(--green)"/>
  </svg>

  <div class="wordmark">
    <span class="wordmark__name">MRF</span>
    <span class="wordmark__sub">ACCOUNTANTS</span>
  </div>

  <div class="band-text" style="left:24px;">Accountant</div>
  <div class="band-text" style="left:250px;">Level 5, 8 Corvale Ridge Road Ashgrove Rise Vic 3187</div>
</section>

</body>
</html>
```